M&A Advisory firm needs elegant and powerful letterhead

We need a powerful but elegant letterhead to engage with the international financial industry.

Target Market(s)

New York and International Financial Industry

Industry/Entity Type

Finance

Font styles to use
Other font styles liked:
• Poppins

Requirements
Must have
• 482 W 71st Street 14th Floor New York, NY 10157 O: +1 (212) 555 0147 F: +1 (212) 555 0182

```html
<!DOCTYPE html>
<html lang="en">
<head>
<meta charset="utf-8">
<title>Halcrest Letterhead</title>
<link href="https://fonts.googleapis.com/css2?family=Montserrat:wght@300;400;500;600&display=swap" rel="stylesheet">
<style>
  :root {
    --brand-blue: #1a5296;
    --pale-blue: #d9e2ee;
    --ink: #141414;
    --ink-soft: #2e2e2e;
    --paper: #ffffff;
    --signature-tone: #e4e4e4;
  }
  * { margin: 0; padding: 0; box-sizing: border-box; }
  html, body { width: 900px; height: 1200px; overflow: hidden; background: var(--paper); }
  .letterhead {
    position: relative; width: 900px; height: 1200px; overflow: hidden;
    background: var(--paper); font-family: "Montserrat", sans-serif; color: var(--ink);
  }
  .corner-accent { position: absolute; top: 0; right: 0; }
  .brand { position: absolute; left: 65px; top: 122px; display: flex; align-items: center; gap: 18px; }
  .brand-dot { width: 58px; height: 58px; border-radius: 50%; background: var(--brand-blue); }
  .brand-name { font-size: 60px; font-weight: 500; color: var(--brand-blue); letter-spacing: 1px; line-height: 1; }
  .salutation { position: absolute; left: 69px; top: 354px; font-size: 20px; font-weight: 600; }
  .letter-body { position: absolute; left: 66px; top: 403px; width: 752px; }
  .letter-body p { font-size: 16.4px; line-height: 18.6px; margin-bottom: 21px; }
  .letter-body p.short { color: var(--ink-soft); }
  .letter-body p.gap { margin-bottom: 28px; }
  .closing { position: absolute; left: 69px; top: 862px; font-size: 16px; }
  .signature { position: absolute; left: 65px; top: 898px; width: 180px; height: 88px; background: var(--signature-tone); border-radius: 4px; }
  .footer-block { position: absolute; left: 0; top: 1089px; width: 40px; height: 40px; background: var(--brand-blue); }
  .contact-phones { position: absolute; left: 64px; top: 1085px; font-size: 18px; font-weight: 300; line-height: 27px; }
  .contact-phones li { list-style: none; display: flex; align-items: center; gap: 8px; }
  .contact-phones svg { width: 16px; height: 16px; fill: var(--brand-blue); }
  .footer-divider { position: absolute; left: 326px; top: 1088px; width: 2px; height: 42px; background: var(--brand-blue); }
  .contact-address { position: absolute; left: 343px; top: 1087px; font-size: 18px; font-weight: 300; line-height: 25px; font-style: normal; }
</style>
</head>
<body>
<main class="letterhead">
  <svg class="corner-accent" width="160" height="170" viewBox="0 0 160 170" aria-hidden="true">
    <circle cx="117" cy="78" r="83" fill="var(--pale-blue)"/>
  </svg>

  <header class="brand">
    <span class="brand-dot"></span>
    <span class="brand-name">HALCREST</span>
  </header>

  <p class="salutation">Dear Mr Hale,</p>

  <section class="letter-body">
    <p>Lorem ipsum dolor sit amet, consectetuer adipiscing elit, sed diam nonummy nibh euis&shy;mod tincidunt ut laoreet dolore magna aliquam erat volutpat. Ut wisi enim ad minim veniam, quis nostrud exerci tation ullamcorper suscipit lobortis nisl ut aliquip ex ea com&shy;modo consequat. Duis autem vel eum iriure dolor in hendrerit in vulputate velit esse molestie consequat, vel illum dolore eu feugiat nulla facilisis at vero eros et accumsan et iusto odio dignissim qui blandit prae</p>
    <p>Lorem ipsum dolor sit amet, consectetuer adipiscing elit, sed diam nonummy nibh euis&shy;mod tincidunt ut laoreet dolore magna aliquam erat volutpat. Ut wisi enim ad minim veniam, quis nostrud exerci tation ullamcorper suscipit lobortis nisl ut aliquip ex ea com&shy;modo consequat. Duis autem vel eum iriure dolor in hendrerit in vulputate velit esse molestie consequat, vel illum dolore eu feugiat nulla facilisis at vero eros et accumsan et iusto odio dignissim qui blandit prae</p>
    <p class="short gap">Lorem ipsum dolor sit amet, consectetuer adipiscing elit, sed diam nonummy nibh euis&shy;mod tincidunt ut laoreet dolore magna aliquam erat volutpat. Ut wisi enim ad minim veniam, quis nostrud exerci tation ullamcorper suscipit lobortis nisl ut aliquip ex ea com-</p>
    <p class="short">Lorem ipsum dolor sit amet, consectetuer adipiscing elit, sed diam nonummy nibh euis&shy;mod tincidunt ut laoreet dolore magna aliquam erat volutpat. Ut wisi enim ad minim veniam, quis nostrud exerci tation ullamcorper suscipit lobortis nisl ut aliquip ex ea com-</p>
  </section>

  <p class="closing">Regards</p>
  <div class="signature" role="img" aria-label="Handwritten signature of the sender"></div>

  <footer>
    <span class="footer-block"></span>
    <ul class="contact-phones">
      <li><svg viewBox="0 0 16 16" aria-hidden="true"><path d="M1 6c0-2 3-4 7-4s7 2 7 4v1h-4V5H5v2H1z"/><rect x="3" y="8" width="10" height="6" rx="1"/></svg>+1 (212) 555 0147</li>
      <li><svg viewBox="0 0 16 16" aria-hidden="true"><rect x="2" y="6" width="12" height="8" rx="1"/><rect x="5" y="2" width="6" height="4"/></svg>+1 (212) 555 0182</li>
    </ul>
    <span class="footer-divider"></span>
    <address class="contact-address">482 W 71st Street 14th Floor<br>New York, NY 10157</address>
  </footer>
</main>
</body>
</html>
```